Modern Website for Brightfield Energy Company

We are a new Brightfield division to an existing construction company. We need a modern but simple design. Visually appealing as the text content will be limited, but we need a visually attractive site. Approx 3 pages (About us, Services, contact) We need some generic photos, drawings etc. of solar panels/installations/how it works. Company Logos attached in .eps format (No/clear Background in logo for use with any background colours). Also company colours (we use this at the bottom of pages as a footer)

Target Market(s)

Private Homeowners + Company Owners in the Middle East (Dubai)

Industry/Entity Type

Brightfield Energy

Coding

Coded - Design and coding required

Number of Pages Required

3 page

Requirements
Must have
• Generic Photos of solar panels, installations, equipment etc.
• Layout similar to fernplot "dot" com
Nice to have
• Maybe a visual representation of how solar works? Maybe an Infographic?? https://www.quorvinex.example/find?q=how+solar+works&espv=2&biw=1600&bih=767&tbm=isch&tbo=u&source=univ&sa=X&ved=0bhVLFxk8sLQIxQUMBiYRCLeNTxQLRWNTEn9RtBRJOR

```html
<!DOCTYPE html>
<html lang="en">
<head>
<meta charset="utf-8">
<title>Brightfield – Solar Energy</title>
<link href="https://fonts.googleapis.com/css2?family=Roboto:wght@400;500;700&family=Roboto+Slab:wght@400;700&family=Noto+Serif:wght@400;700&display=swap" rel="stylesheet">
<style>
:root{
  --green:#8cc63f;
  --green-dark:#6ea52a;
  --ink:#222;
  --muted:#777;
  --dark:#151515;
  --dark-2:#1e1e1e;
  --light:#f6f6f6;
  --red:#e5472c;
  --white:#fff;
}
*{box-sizing:border-box;margin:0;padding:0}
html,body{width:1200px;height:5085px;overflow:hidden}
body{position:relative;font-family:"Noto Serif",serif;color:var(--ink);background:var(--white);font-size:13px;line-height:1.6}
.abs{position:absolute}
h2.section-title{font-family:"Roboto Slab",serif;font-weight:700;font-size:28px;text-align:center;color:var(--ink)}
.section-rule{width:34px;height:2px;background:var(--red);margin:0 auto 18px}
.section-sub{text-align:center;color:var(--muted);font-size:12px;margin-top:6px}

/* header */
.site-header{top:0;left:0;width:1200px;height:68px;background:var(--white);z-index:5;box-shadow:0 1px 3px rgba(0,0,0,.08)}
.brand{left:0;top:0;width:170px;height:68px;background:var(--green);display:flex;align-items:center;gap:10px;padding-left:26px}
.brand-dot{width:14px;height:14px;background:var(--white);border-radius:50%}
.brand-name{font-family:"Roboto",sans-serif;font-weight:700;font-size:18px;color:var(--white)}
.main-nav{left:300px;top:0;height:68px;display:flex;align-items:center;gap:30px;font-family:"Roboto",sans-serif;font-size:12px;font-weight:500;color:#555;text-transform:uppercase}
.main-nav .active{color:var(--green)}
.social-bar{right:0;top:0;width:200px;height:68px;background:var(--green);display:flex;align-items:center;justify-content:center;gap:26px}
.social-bar span{width:14px;height:14px;border-radius:50%;background:var(--white)}

/* hero */
.hero{top:68px;left:0;width:1200px;height:587px;background:linear-gradient(100deg,#2d3b4a 0%,#5a4a3a 35%,#8a5a30 60%,#3a2a20 100%)}
.hero-tag{left:70px;top:260px;font-family:"Roboto",sans-serif;font-size:12px;color:var(--green);font-weight:700;letter-spacing:1px}
.hero-title{left:66px;top:282px;width:520px;font-family:"Roboto",sans-serif;font-weight:700;font-size:44px;line-height:1.12;color:var(--white)}
.btn{display:inline-block;font-family:"Roboto",sans-serif;font-weight:700;font-size:12px;letter-spacing:1px;text-transform:uppercase;color:var(--white);background:var(--green);border-radius:3px;padding:10px 24px}
.hero .btn{position:absolute;left:70px;top:460px}
.hero-points{left:935px;top:105px;width:230px;font-family:"Roboto",sans-serif}
.hero-points li{list-style:none;margin-bottom:30px}
.hero-points b{display:block;font-size:10px;color:var(--green);letter-spacing:1px;text-transform:uppercase}
.hero-points p{font-size:16px;line-height:1.25;color:var(--white)}
.hero-points .on p{font-weight:700}
.hero-arrows{right:30px;bottom:18px;display:flex;gap:14px}

/* provide section */
.provide{top:655px;left:0;width:1200px;height:667px}
.sector-card{top:915px;width:358px;height:340px;border:1px solid #e3e3e3;background:var(--white);text-align:center;padding:178px 40px 0}
.diamond{top:895px;width:140px;height:140px;transform:rotate(45deg);border:6px solid var(--white);box-shadow:0 0 0 1px #ddd;overflow:hidden;z-index:2}
.sector-card h3{font-family:"Roboto Slab",serif;font-size:15px;font-weight:700;text-transform:uppercase;margin-bottom:10px}
.sector-card h3::after{content:"";display:block;width:30px;height:2px;background:var(--green);margin:8px auto 0}
.sector-card p{font-size:12px;color:var(--muted)}

/* planet band */
.planet{top:1322px;left:0;width:1200px;height:628px;background:linear-gradient(180deg,#5f8f2e 0%,#7fb23c 45%,#a7cf72 80%,#eef3e6 100%);border-top:3px solid var(--green)}
.planet h2{position:absolute;top:128px;width:100%;text-align:center;font-family:"Roboto Slab",serif;font-size:26px;color:var(--white)}
.planet p{position:absolute;top:215px;left:360px;width:480px;text-align:center;color:var(--white);font-size:11px;line-height:1.7}
.bulb{left:360px;top:1680px;width:480px;height:320px;border-radius:45% 55% 40% 40%;background:radial-gradient(ellipse at 45% 45%,#eef5fb 0%,#b9cfe0 45%,#6ea52a 75%,rgba(110,165,42,0) 76%)}

/* features */
.features{top:1950px;left:0;width:1200px;height:796px}
.feature{width:250px;height:220px;background:var(--white);box-shadow:0 1px 6px rgba(0,0,0,.1);text-align:center;padding:22px 26px 0}
.feature svg{width:52px;height:52px;stroke:#333;fill:none;stroke-width:1.6}
.feature h4{font-family:"Roboto Slab",serif;font-size:14px;margin:16px 0 8px}
.feature p{font-size:11px;color:var(--muted);line-height:1.55}

/* projects */
.projects{top:2746px;left:0;width:1200px;height:780px;background:linear-gradient(180deg,#111 0%,#1b1b1b 100%)}
.projects .section-title{color:var(--white);padding-top:130px}
.projects .section-sub{color:#aaa;width:460px;margin:12px auto 0}
.project{top:3000px;width:366px;height:339px;background:var(--white)}
.project .photo{height:237px}
.project h4{font-family:"Roboto Slab",serif;font-size:15px;text-align:center;margin-top:24px}
.project small{display:block;text-align:center;font-family:"Roboto",sans-serif;font-size:10px;color:var(--muted);letter-spacing:1px}
.projects .btn{position:absolute;left:500px;top:622px;width:200px;text-align:center}

/* news */
.news{top:3526px;left:0;width:1200px;height:678px}
.news .section-title{padding-top:124px}
.news .section-sub{width:460px;margin:12px auto 0}
.post{top:3763px;width:366px;height:390px;background:var(--white)}
.post .photo{height:197px;position:relative}
.post .date{position:absolute;left:12px;top:0;width:40px;height:40px;background:var(--green);color:var(--white);font-family:"Roboto",sans-serif;font-weight:700;font-size:14px;display:flex;align-items:center;justify-content:center}
.post h4{font-family:"Roboto Slab",serif;font-size:15px;margin:24px 0 10px}
.post p{font-size:11px;color:var(--muted);line-height:1.6}
.post .more{position:absolute;right:0;bottom:22px;color:var(--green);font-size:12px;font-weight:700}

/* offers */
.offers{top:4255px;left:0;width:1200px;height:457px;background:var(--green)}
.offers h2{position:absolute;left:50px;top:145px;font-family:"Roboto",sans-serif;font-size:26px;color:var(--white)}
.offers p{position:absolute;left:50px;top:210px;width:520px;color:var(--white);font-size:11px}
.field{position:absolute;top:270px;width:255px;height:36px;background:var(--white);border-radius:2px;padding:9px 12px;color:#999;font-size:11px}
.btn-red{position:absolute;left:50px;top:325px;background:var(--red);color:var(--white);font-family:"Roboto",sans-serif;font-weight:700;font-size:11px;letter-spacing:1px;padding:10px 26px;border-radius:2px}
.offer-visual{left:620px;top:4190px;width:520px;height:522px;background:linear-gradient(160deg,#2b4d7a 0%,#1b355c 55%,#4f7f2a 100%)}

/* footer */
.site-footer{top:4712px;left:0;width:1200px;height:373px;background:var(--dark);color:#bbb}
.footer-col{top:92px;font-size:11px;line-height:1.8}
.footer-col h5{font-family:"Roboto",sans-serif;font-size:13px;color:var(--white);letter-spacing:1px;margin-bottom:14px}
.footer-brand{font-family:"Roboto",sans-serif;font-weight:700;font-size:22px;color:var(--white);display:flex;align-items:center;gap:8px;margin-bottom:12px}
.footer-brand i{width:12px;height:12px;background:var(--green);display:block}
.footer-col .accent{color:var(--white);font-weight:700}
.news-field{display:flex;margin-top:14px}
.news-field span{width:210px;height:34px;background:#2a2a2a;border:1px solid #333;padding:7px 10px;color:#777}
.news-field b{width:40px;height:34px;background:var(--red);display:flex;align-items:center;justify-content:center}
.footer-social{display:flex;gap:10px;margin-top:14px}
.footer-social span{width:22px;height:22px;border-radius:50%;background:#444}
.footer-bottom{top:278px;left:0;width:1200px;border-top:1px solid #2c2c2c;text-align:center;font-family:"Roboto",sans-serif}
.footer-links{display:flex;justify-content:center;gap:62px;padding-top:22px;color:var(--white);font-size:12px}
.copyright{font-size:10px;color:#777;margin-top:24px}
</style>
</head>
<body>

<header class="site-header abs">
  <div class="brand abs"><span class="brand-dot"></span><span class="brand-name">Brightfield</span></div>
  <nav class="main-nav abs">
    <span class="active">Home</span><span>Pages</span><span>Portfolio</span><span>Blog</span><span>Submenu</span><span>Contact</span><span>Shop</span>
  </nav>
  <div class="social-bar abs"><span></span><span></span><span></span></div>
</header>

<section class="hero abs" role="img" aria-label="Photo of solar panel rows and wind turbines at sunset">
  <div class="hero-tag abs">CLEAN ENERGY</div>
  <h1 class="hero-title abs">We will help you to reduce your energy consumption.</h1>
  <span class="btn">Read More</span>
  <ul class="hero-points abs">
    <li><b>Ecology Awareness</b><p>All our energy is generated from renewable sources.</p></li>
    <li class="on"><b>Natural Beauty</b><p>We will help you to reduce your energy consumption.</p></li>
    <li><b>Choose the Sun</b><p>Walking with a friend in the dark is better than alone in the light.</p></li>
  </ul>
  <div class="hero-arrows abs">
    <svg width="10" height="12" viewBox="0 0 10 12"><path d="M7 1 2 6l5 5" stroke="#fff" stroke-width="2" fill="none"/></svg>
    <svg width="10" height="12" viewBox="0 0 10 12"><path d="M3 1l5 5-5 5" stroke="#fff" stroke-width="2" fill="none"/></svg>
  </div>
</section>

<section class="provide abs">
  <div class="section-rule" style="margin-top:72px"></div>
  <h2 class="section-title">We Provide Energy</h2>
  <p class="section-sub">To many clients like government, homes and offices</p>
</section>

<div class="diamond abs" style="left:136px;background:linear-gradient(135deg,#9db8c9,#c8a77a)" role="img" aria-label="Photo of a government office building"></div>
<div class="diamond abs" style="left:530px;background:linear-gradient(135deg,#4f7ea8,#a9c0d0)" role="img" aria-label="Photo of solar panels on a house roof"></div>
<div class="diamond abs" style="left:924px;background:linear-gradient(135deg,#8a4a30,#c9b08a)" role="img" aria-label="Photo of a commercial building with rooftop panels"></div>

<article class="sector-card abs" style="left:27px"><h3>Government</h3><p>As the world's largest green and clean energy specialist of the printing and typesetting industry. Lorem has been the industry.</p></article>
<article class="sector-card abs" style="left:421px"><h3>Residential</h3><p>As the world's largest green and clean energy specialist of the printing and typesetting industry. Lorem has been the industry.</p></article>
<article class="sector-card abs" style="left:815px"><h3>Commercial</h3><p>As the world's largest green and clean energy specialist of the printing and typesetting industry. Lorem has been the industry.</p></article>

<section class="planet abs" role="img" aria-label="Green field with wind turbines">
  <h2>SAVE THE PLANET!</h2>
  <p>Sed posuere consectetur est at lobortis. Nullam id dolor id nibh ultricies vehicula ut id elit. Maecenas sed diam eget risus varius blandit sit amet non magna. Donec ullamcorper nulla non metus auctor fringilla vel eu leo.</p>
</section>
<div class="bulb abs" role="img" aria-label="Light bulb lying on grass with a sprout inside"></div>

<section class="features abs">
  <div class="section-rule" style="margin-top:130px"></div>
  <h2 class="section-title">We Provide Energy</h2>
  <p class="section-sub">To many clients like government, homes and offices</p>
</section>

<div class="feature abs" style="left:50px;top:2197px">
  <svg viewBox="0 0 52 52"><circle cx="26" cy="26" r="20"/><circle cx="26" cy="26" r="9"/><path d="M12 12l8 8M40 12l-8 8M12 40l8-8M40 40l-8-8"/></svg>
  <h4>Awesome Services</h4><p>Our services are as awesome of passages of Lorem Ipsum available.</p></div>
<div class="feature abs" style="left:332px;top:2197px">
  <svg viewBox="0 0 52 52"><path d="M26 6a14 14 0 0 0-8 25v7h16v-7a14 14 0 0 0-8-25zM20 42h12M22 46h8"/></svg>
  <h4>Get Unlimited Energy</h4><p>Get Unlimited Energy of passages of Lorem Ipsum available.</p></div>
<div class="feature abs" style="left:614px;top:2197px">
  <svg viewBox="0 0 52 52"><path d="M26 5l6 14 15 1-11 10 4 15-14-8-14 8 4-15L5 20l15-1z"/></svg>
  <h4>Fist Class Support</h4><p>There is many variantions of passages of Lorem Ipsum available.</p></div>
<div class="feature abs" style="left:896px;top:2197px">
  <svg viewBox="0 0 52 52"><circle cx="26" cy="26" r="20"/><ellipse cx="26" cy="26" rx="9" ry="20"/><path d="M6 26h40M9 16h34M9 36h34"/></svg>
  <h4>Save the Palnet</h4><p>There is many variantions of passages of Lorem Ipsum available.</p></div>

<div class="feature abs" style="left:50px;top:2441px">
  <svg viewBox="0 0 52 52"><path d="M4 18h30a6 6 0 1 0-6-6M4 28h40a6 6 0 1 1-6 6M4 38h22"/></svg>
  <h4>Wind Energy</h4><p>There is many variantions of passages of Lorem Ipsum available.</p></div>
<div class="feature abs" style="left:332px;top:2441px">
  <svg viewBox="0 0 52 52"><circle cx="26" cy="26" r="9"/><path d="M26 5v7M26 40v7M5 26h7M40 26h7M11 11l5 5M36 36l5 5M11 41l5-5M36 16l5-5"/></svg>
  <h4>Reduced Costs</h4><p>There is many variantions of passages of Lorem Ipsum available.</p></div>
<div class="feature abs" style="left:614px;top:2441px">
  <svg viewBox="0 0 52 52"><path d="M8 44l20-20M30 8a9 9 0 0 0 12 12l-6 2-6-6zM10 8l10 10M44 44L30 30"/></svg>
  <h4>Easy Maintenance</h4><p>There is many variantions of passages of Lorem Ipsum available.</p></div>
<div class="feature abs" style="left:896px;top:2441px">
  <svg viewBox="0 0 52 52"><path d="M30 4L12 30h12l-4 18 20-28H28z"/></svg>
  <h4>Power Energy</h4><p>There is many variantions of passages of Lorem Ipsum available.</p></div>

<section class="projects abs">
  <h2 class="section-title">Latest Projects</h2>
  <div class="section-rule" style="margin-top:12px;margin-bottom:0"></div>
  <p class="section-sub">Sed ut perspiciatis unde omnis iste natus error sit voluptatem accusantium doloremque laudantium, totam rem aperiam.</p>
  <span class="btn">&#8801;&nbsp; More Project</span>
</section>

<article class="project abs" style="left:34px"><div class="photo" role="img" aria-label="Photo of solar panels under a sunset sky" style="background:linear-gradient(180deg,#d98a4a,#3f5e86)"></div><h4>Swedish Mega Project</h4><small>DESIGN, INTERIOR, OFFICE</small></article>
<article class="project abs" style="left:417px"><div class="photo" role="img" aria-label="Photo of a solar farm beside wind turbines" style="background:linear-gradient(180deg,#e8c87a,#2f4a6e)"></div><h4>So to deliberately render</h4><small>DESIGN, INTERIOR, OFFICE</small></article>
<article class="project abs" style="left:800px"><div class="photo" role="img" aria-label="Photo of solar panels in front of a city skyline" style="background:linear-gradient(180deg,#c8d8e6,#3c5a82)"></div><h4>Frozen Trees In A Lake</h4><small>DESIGN, INTERIOR, OFFICE</small></article>

<section class="news abs">
  <h2 class="section-title">Our Latest News</h2>
  <div class="section-rule" style="margin-top:12px;margin-bottom:0"></div>
  <p class="section-sub">Sed ut perspiciatis unde omnis iste natus error sit voluptatem accusantium doloremque laudantium, totam rem aperiam.</p>
</section>

<article class="post abs" style="left:34px"><div class="photo" role="img" aria-label="Photo of engineers planning a solar installation" style="background:linear-gradient(135deg,#c9d6e2,#3a6fa8)"><span class="date">26</span></div><h4>Dignissim phasellus ultrices tellus</h4><p>Sed odio orci, fringilla nec dolor at, commodo auctor mauris. Curabitur semper dui diam, nec accumsan mauris consequat sed. Vestibulum et malesuada lorem ut ante.</p><span class="more">Read More &rarr;</span></article>
<article class="post abs" style="left:417px"><div class="photo" role="img" aria-label="Photo of a technician installing rooftop panels" style="background:linear-gradient(135deg,#8fb3d6,#2b4f7c)"><span class="date">26</span></div><h4>Excepteur sint occaecat cupidatat</h4><p>Sed odio orci, fringilla nec dolor at, commodo auctor mauris. Curabitur semper dui diam, nec accumsan mauris consequat sed. Vestibulum et malesuada lorem ut ante.</p><span class="more">Read More &rarr;</span></article>
<article class="post abs" style="left:800px"><div class="photo" role="img" aria-label="Photo of wind turbines over a yellow field" style="background:linear-gradient(180deg,#b8d4ec,#c9b24a)"><span class="date">26</span></div><h4>Aenean nonummy hendrerit mauris</h4><p>Sed odio orci, fringilla nec dolor at, commodo auctor mauris. Curabitur semper dui diam, nec accumsan mauris consequat sed. Vestibulum et malesuada lorem ut ante.</p><span class="more">Read More &rarr;</span></article>

<section class="offers abs">
  <h2>Get Latest Offers</h2>
  <p>Sed odio orci, fringilla nec dolor at, commodo auctor mauris. Curabitur semper dui diam, nec accumsan mauris consequat sed. Vestibulum et malesuada lorem.</p>
  <span class="field" style="left:50px">Your Name</span>
  <span class="field" style="left:330px">Your Email</span>
  <span class="btn-red">SUBSCRIBE</span>
</section>
<div class="offer-visual abs" role="img" aria-label="Smiling installer standing beside a large solar panel"></div>

<footer class="site-footer abs">
  <div class="footer-col abs" style="left:50px;width:300px;top:100px">
    <div class="footer-brand"><i></i>Brightfield</div>
    <p>The solar is the leader of green energy in the country and clean economy focused integer tincidunt of labore and efficient strategy.</p>
    <p style="margin-top:8px">We provide the energy to medium and big companies, multipoint offer, and client economy.</p>
  </div>
  <div class="footer-col abs" style="left:425px;width:330px">
    <h5>GET IN TOUCH</h5>
    <p><span class="accent">PHONE:</span> +00 555 0142 77</p>
    <p><span class="accent">FAX:</span> +00 555 0142 78</p>
    <p><span class="accent">EMAIL:</span> hello@brightfield-power.example</p>
    <p><span class="accent">ADRESS:</span> 12 Palm Row, Sunport 0400</p>
    <div class="footer-social"><span></span><span></span><span></span></div>
  </div>
  <div class="footer-col abs" style="left:800px;width:330px">
    <h5>NEWSLETTER</h5>
    <p class="accent" style="font-weight:400;color:#ddd">SIGN UP YOUR NEWSLETTER</p>
    <div class="news-field"><span>EMAIL ADRESS</span><b><svg width="12" height="12" viewBox="0 0 12 12"><path d="M2 6h8M7 3l3 3-3 3" stroke="#fff" stroke-width="1.6" fill="none"/></svg></b></div>
  </div>
  <div class="footer-bottom abs">
    <div class="footer-links"><span>Home</span><span>About Us</span><span>Blog</span><span>Contact</span></div>
    <p class="copyright">&copy; 2016 Brightfield. All rights reserved.</p>
  </div>
</footer>

</body>
</html>
```